Youth organisation needs design work for awards booklet

We are from The Kestrel Guild in Singapore, and we need design work for an awards booklet for one of our most prestigious awards, the Lodestar Award. This booklet will comprise of the list of the recipients, congratulatory notes and stories from some of the recipients. This booklet will be printed for each of the recipient to keep as a remembrance. We are looking for dual or tri-colour scheme, with bronze being one of the colours.

Recipients of the Award, school Principals and teachers

• We are looking to have around 16 designed pages, including front and back cover. Size of the booklet is:
Closed - W100mm x H210mm; Opened - W200mm x H210mm
Cover page - picture of the Award
Page 2-3 - two congratulatory notes
Page 4-5 - picture of the Award and description of the Award
Page 6-7 - Testimonials
Page 8-14 - List of recipients (to be provided upon confirmation of designer)
Page 15 - blank page or acknowledgments page
Back Cover - KG Logo and contact details
(Refer to previous years' booklets for reference)

Designers can submit just the cover pages as well as 1 sample inner page to get a sense of the overall style of design during the selection round.
• Clean, prestigious/premium look

```html
<!DOCTYPE html>
<html lang="en">
<head>
<meta charset="utf-8">
<title>Lodestar Award Presentation Ceremony – Cover</title>
<link rel="stylesheet" href="https://fonts.googleapis.com/css2?family=Jost:wght@500;600;700&family=Montserrat:wght@600;700&family=Open+Sans:wght@400&family=Yellowtail&display=swap">
<style>
  :root {
    --gold-deep: #b8842f;
    --gold-mid: #d9a95a;
    --gold-light: #f0c98a;
    --cream: #f6e3a6;
    --cream-shadow: rgba(90, 55, 10, 0.55);
    --ink: #1c1c1f;
    --ink-soft: #2a2522;
    --spine: #5a3a14;
    --tab-dark: #5b3a0e;
    --tab-bright: #f3b33c;
    --pill-light: #fbf4d4;
    --pill-edge: #d8b764;
  }
  * { margin: 0; padding: 0; box-sizing: border-box; }
  html, body { width: 1143px; height: 1200px; overflow: hidden; background: #fff; }

  .booklet-spread {
    position: relative;
    width: 1143px;
    height: 1200px;
    background:
      radial-gradient(ellipse 70% 55% at 30% 48%, rgba(255, 214, 150, 0.55), transparent 70%),
      radial-gradient(ellipse 60% 50% at 80% 40%, rgba(255, 220, 160, 0.35), transparent 70%),
      linear-gradient(180deg, var(--gold-mid) 0%, var(--gold-light) 45%, var(--gold-mid) 75%, var(--gold-deep) 100%);
    overflow: hidden;
  }

  .spine-line {
    position: absolute;
    left: 571px; top: 0;
    width: 1px; height: 1200px;
    background: var(--spine);
  }

  .closure-tab {
    position: absolute;
    left: 534px; top: 309px;
    width: 75px; height: 631px;
    border-radius: 38px;
    background: linear-gradient(90deg, var(--tab-dark) 0%, #a5711f 35%, var(--tab-bright) 60%, #c78a25 80%, var(--tab-dark) 100%);
    box-shadow: 0 2px 6px rgba(60, 35, 5, 0.35);
  }

  /* Back cover */
  .back-cover {
    position: absolute;
    left: 0; top: 0;
    width: 571px; height: 1200px;
    text-align: center;
  }
  .org-mark {
    position: absolute;
    left: 226px; top: 470px;
    width: 120px; height: 120px;
    border-radius: 50%;
    background: var(--ink-soft);
    opacity: 0.85;
  }
  .org-name {
    position: absolute;
    left: 0; right: 0; top: 660px;
    font-family: "Montserrat", sans-serif;
    font-weight: 700;
    font-size: 27px;
    letter-spacing: 1px;
    color: var(--ink-soft);
  }
  .contact-address {
    position: absolute; left: 0; right: 0; top: 736px;
    font-family: "Montserrat", sans-serif; font-weight: 700;
    font-size: 21px; color: var(--ink);
  }
  .contact-line {
    position: absolute; left: 0; right: 0;
    font-family: "Montserrat", sans-serif; font-weight: 700;
    font-size: 17px; color: var(--ink);
  }
  .contact-phone { top: 770px; }
  .contact-email { top: 799px; }

  /* Front cover */
  .front-cover {
    position: absolute;
    left: 572px; top: 0;
    width: 571px; height: 1200px;
    text-align: center;
  }
  .title-stars {
    position: absolute; top: 58px;
    display: flex; gap: 4px;
  }
  .title-stars svg { width: 26px; height: 26px; fill: var(--cream); filter: drop-shadow(1px 2px 1px var(--cream-shadow)); }
  .title-stars--left { left: 88px; }
  .title-stars--right { left: 344px; }
  .title-the {
    position: absolute; left: 0; right: 0; top: 52px;
    font-family: "Yellowtail", cursive;
    font-size: 38px; color: var(--cream);
    text-shadow: 1px 2px 2px var(--cream-shadow);
  }
  .title-main {
    position: absolute; left: 0; right: 0; top: 92px;
    font-family: "Jost", sans-serif; font-weight: 600;
    font-size: 60px; line-height: 1;
    color: var(--cream);
    text-shadow: 2px 3px 3px var(--cream-shadow);
  }
  .title-sub {
    position: absolute; left: 20px; right: 0; top: 152px;
    font-family: "Jost", sans-serif; font-weight: 600;
    font-size: 31px; letter-spacing: 7.5px;
    color: var(--cream);
    text-shadow: 2px 3px 3px var(--cream-shadow);
  }

  .award-medal-photo {
    position: absolute;
    left: 65px; top: 274px;
    width: 430px; height: 576px;
    border-radius: 48% 48% 46% 46% / 40% 40% 48% 48%;
    background: radial-gradient(circle at 45% 55%, #cfc7b8 0%, #9b9385 45%, #6e675c 75%, #4b463f 100%);
    box-shadow: 3px 6px 10px rgba(60, 35, 5, 0.4);
  }

  .guest-label {
    position: absolute; left: 0; right: 0; top: 872px;
    font-family: "Montserrat", sans-serif; font-weight: 700;
    font-size: 22px; color: var(--ink);
  }
  .guest-name {
    position: absolute; left: 0; right: 0; top: 893px;
    font-family: "Montserrat", sans-serif; font-weight: 700;
    font-size: 37px; color: var(--ink);
  }
  .guest-roles {
    position: absolute; left: 0; right: 0; top: 960px;
    font-family: "Open Sans", sans-serif; font-weight: 400;
    font-size: 22px; line-height: 25px; color: var(--ink);
  }

  .venue-pill {
    position: absolute;
    left: 106px; top: 1066px;
    width: 357px; height: 58px;
    border-radius: 29px;
    background: linear-gradient(90deg, var(--pill-edge) 0%, var(--pill-light) 35%, #fffbe8 60%, var(--pill-edge) 100%);
    box-shadow: 2px 4px 6px rgba(60, 35, 5, 0.3);
    font-family: "Montserrat", sans-serif; font-weight: 700;
    color: var(--ink);
    padding-top: 3px;
  }
  .venue-room { font-size: 26px; line-height: 28px; }
  .venue-club { font-size: 21px; line-height: 24px; }

  .event-date {
    position: absolute; left: 0; right: 0; top: 1134px;
    font-family: "Yellowtail", cursive;
    font-size: 36px; color: var(--cream);
    text-shadow: 1px 2px 2px var(--cream-shadow);
  }
</style>
</head>
<body>
<main class="booklet-spread">
  <section class="back-cover">
    <div class="org-mark"></div>
    <p class="org-name">THE KESTREL GUILD</p>
    <p class="contact-address">48 Wren Lane, Singapore 238812</p>
    <p class="contact-line contact-phone">Tel:(65) 6100 2000 | Fax: (65) 6100 2001</p>
    <p class="contact-line contact-email">Email:office@kestrelguild.sg</p>
  </section>

  <div class="spine-line"></div>
  <div class="closure-tab"></div>

  <section class="front-cover">
    <div class="title-stars title-stars--left">
      <svg viewBox="0 0 24 24"><path d="M12 2l2.9 6.6 7.1.6-5.4 4.7 1.6 7-6.2-3.8-6.2 3.8 1.6-7L2 9.2l7.1-.6z"/></svg>
      <svg viewBox="0 0 24 24"><path d="M12 2l2.9 6.6 7.1.6-5.4 4.7 1.6 7-6.2-3.8-6.2 3.8 1.6-7L2 9.2l7.1-.6z"/></svg>
      <svg viewBox="0 0 24 24"><path d="M12 2l2.9 6.6 7.1.6-5.4 4.7 1.6 7-6.2-3.8-6.2 3.8 1.6-7L2 9.2l7.1-.6z"/></svg>
    </div>
    <p class="title-the">The</p>
    <div class="title-stars title-stars--right">
      <svg viewBox="0 0 24 24"><path d="M12 2l2.9 6.6 7.1.6-5.4 4.7 1.6 7-6.2-3.8-6.2 3.8 1.6-7L2 9.2l7.1-.6z"/></svg>
      <svg viewBox="0 0 24 24"><path d="M12 2l2.9 6.6 7.1.6-5.4 4.7 1.6 7-6.2-3.8-6.2 3.8 1.6-7L2 9.2l7.1-.6z"/></svg>
      <svg viewBox="0 0 24 24"><path d="M12 2l2.9 6.6 7.1.6-5.4 4.7 1.6 7-6.2-3.8-6.2 3.8 1.6-7L2 9.2l7.1-.6z"/></svg>
    </div>
    <h1 class="title-main">LODESTAR AWARD</h1>
    <p class="title-sub">PRESENTATION CEREMONY</p>

    <div class="award-medal-photo" role="img" aria-label="Photograph of the silver Lodestar Award medal"></div>

    <p class="guest-label">Guests-Of-Honour</p>
    <p class="guest-name">Mr Tan Wei Ming</p>
    <p class="guest-roles">Senior Parliamentary Secretary,<br>Office of Community and Youth<br>Office of Urban Mobility</p>

    <div class="venue-pill">
      <p class="venue-room">Grand Ballroom</p>
      <p class="venue-club">Palmgrove Country Club</p>
    </div>

    <p class="event-date">6 July 2020</p>
  </section>
</main>
</body>
</html>
```